Real estate company needs a letterhead design

A young real estate company needs a letterhead / stationery design, it should include the company's logo. It should look exactly the same as on the business cards. (With the phrase "a brand of KEV Wohnbau & Grundstücksentwicklung GmbH")

In addition, it should also include the 4 round seals.

color code blue # 00456b gray # 333333

Word and PDF are welcome.

KEV Wohnbau & Grundstücksentwicklung GmbH
Managing director: Mag. Lukas Fellnhuber
Matthias-Ortner-Strasse 3c / 41
6300 Wörgl

Tel .: +436648172093
Email: office@wohnglanz-beispiel.at
Web: www.wohnglanz-beispiel.at

Sparkasse Almtal, Bergländer Sparkasse from 1882, Genossenschaftskasse
Anton-Weissauer-Strasse 7, 6300 Wörgl
IBAN: AT31 4817 2964 0058 2316
BIC: GLMTAT44XXX
Account holder: KEV Wohnbau & Grundstücksentwicklung GmbH

FN: XXXXXXX
UID: XXXXXXX

```html
<!DOCTYPE html>
<html lang="de">
<head>
<meta charset="utf-8">
<title>Wohnglanz Letterhead</title>
<link rel="stylesheet" href="https://fonts.googleapis.com/css2?family=Arimo:wght@400;700&family=Montserrat:wght@300;400;700&display=swap">
<style>
  :root {
    --brand-blue: #00456b;
    --brand-gray: #333333;
    --text-light: #9a9a9a;
    --backdrop: #eef2f6;
    --paper: #ffffff;
  }
  * { box-sizing: border-box; margin: 0; padding: 0; }
  html, body { width: 1200px; height: 1200px; overflow: hidden; background: var(--backdrop); }
  .sheet {
    position: absolute; left: 196px; top: 30px;
    width: 846px; height: 1196px;
    transform: scale(0.953); transform-origin: top left;
    background: var(--paper);
    font-family: "Montserrat", sans-serif;
    box-shadow: 0 2px 10px rgba(0,0,0,.12);
  }
  .header-waves { position: absolute; left: 0; top: 0; width: 846px; height: 200px; }
  .bank-address {
    position: absolute; right: 71px; top: 26px;
    text-align: right; color: #fff;
    font-family: "Arimo", sans-serif; font-size: 14.5px; line-height: 17px;
  }
  .brand { position: absolute; left: 50px; top: 128px; }
  .brand-row { display: flex; align-items: center; gap: 10px; }
  .brand-dot { width: 22px; height: 22px; border-radius: 50%; background: var(--brand-blue); flex: none; }
  .brand-name {
    font-family: "Montserrat", sans-serif; font-weight: 400;
    font-size: 32px; color: var(--brand-gray); letter-spacing: 1px; line-height: 38px;
  }
  .brand-tagline { font-size: 9.5px; color: var(--brand-gray); margin-top: 4px; }
  .recipient { position: absolute; left: 85px; top: 267px; }
  .recipient-label { font-size: 14px; letter-spacing: 2px; color: var(--brand-gray); }
  .recipient-name { font-size: 14.5px; color: var(--brand-blue); margin-top: 6px; }
  .recipient-address { font-size: 11.5px; font-weight: 300; color: var(--text-light); line-height: 19px; margin-top: 4px; }
  .letter-date { position: absolute; right: 87px; top: 266px; font-size: 12px; color: #555; }
  .letter-body { position: absolute; left: 85px; top: 427px; width: 676px; }
  .letter-body p {
    font-size: 12px; font-weight: 300; line-height: 15px;
    color: var(--text-light); text-align: justify; margin-bottom: 15px;
  }
  .signature-mark { position: absolute; left: 85px; top: 845px; width: 145px; height: 36px; }
  .signer { position: absolute; left: 83px; top: 890px; }
  .signer-name { font-size: 14px; color: var(--brand-gray); }
  .signer-role { font-size: 11px; font-weight: 300; color: var(--text-light); margin-top: 3px; }
  .footer {
    position: absolute; left: 55px; top: 1098px; display: flex;
    font-family: "Arimo", sans-serif; font-size: 13px; line-height: 16.3px; color: #222;
  }
  .footer-col { padding-right: 20px; }
  .footer-col + .footer-col { border-left: 1px solid #555; padding-left: 20px; }
  .footer-col b { color: var(--brand-blue); font-weight: 700; }
</style>
</head>
<body>
<main class="sheet">
  <svg class="header-waves" viewBox="0 0 846 200" aria-hidden="true">
    <path fill="var(--brand-blue)" d="M0,0 H846 V65 C770,150 650,160 520,118 C390,74 270,22 150,38 C80,48 30,88 0,140 Z"/>
    <path fill="var(--brand-gray)" d="M102,54 C250,38 390,82 525,128 C660,172 790,160 846,102 V112 C800,168 700,192 560,162 C420,126 260,62 102,54 Z"/>
  </svg>

  <div class="bank-address">
    Sparkasse Almtal<br>
    Bergländer Sparkasse from 1882<br>
    Genossenschaftskasse<br>
    Anton-Weissauer-Strasse 7<br>
    6300 Wörgl
  </div>

  <div class="brand">
    <div class="brand-row">
      <span class="brand-dot" aria-hidden="true"></span>
      <div class="brand-name">WOHNGLANZ</div>
    </div>
    <div class="brand-tagline">eine Marke der KEV Wohnbau &amp; Grundstücksentwicklung GmbH</div>
  </div>

  <div class="letter-date">Friday, 01/01/2018</div>

  <div class="recipient">
    <div class="recipient-label">TO</div>
    <div class="recipient-name">Tobias Reinhalter</div>
    <div class="recipient-address">
      Human Resources<br>
      Nordhang Systems Ltd.<br>
      2207-B Lindenweg, Haldenau<br>
      F12 USA
    </div>
  </div>

  <section class="letter-body">
    <p>Lorem ipsum dolor sit amet, consectetuer adipiscing elit, sed diam nonmmy nibh euismod tincidunt ut laoreet dolore magna aliquam erat volutpat. Ut wisi enim ad minim veniam, quis nostrud exerci tationmcorper suscipit lobortis nisl ut aliquip ex ea commodo consequat. Duis autem vel eum iriure dolor in hendrerit in vulputate velit esse molestie consequat, vel illum dolore eu feugiat nulla facilisis at vero eros et accumsan et iusto odio dignissim qui blandit praesent luptatum zzril delenit augue duis dolore te feugait nulla facilisi.</p>
    <p>Nam liber tempor cum soluta nobis eleifend option congue nihil imprdiet doming id quod mazim placerat facer possim assum. Typi non habent claritatem insitam;</p>
    <p>Est usus legentis in iis qui facit eorum claritatem.</p>
    <p>Investigationes demonstraverunt lectores legere me lius quod ii legunt saepius. Claritas est etiam processus dynamicus, qui sequitur mutationem consuetudium lectorum. Mirum est notare quam littera gothica, quam nunc putamus parum claram, anteposuerit litterarum formas humanitatis per seacula quarta decima et quinta decima. Eodem modo typi, qui nunc nobis videntur parum clari, fiant sollemnes in futurum.</p>
    <p>consectetuer adipiscing elit, sed diam nonummy nibh euismod tincidunt ut laoreet dolore magna aliquam erat volutpat. Ut wisi enim ad minim veniam, quis nostrud exerci tation ullamcorper suscipit lobortis nisl ut aliquip ex ea commodo consequat. Duis autem vel eum iriure dolor in hendrerit in vulputate velit esse molestie consequat, vel illum dolore eu feugiat nulla facilisis at vero eros et accumsan et iusto odio dignissim qui blandit praesent luptatum zzril delenit augue duis dolore te feugait nulla facilisi.</p>
    <p>Nam liber tempor cum soluta nobis eleifend option congue nihil imperdiet .</p>
  </section>

  <svg class="signature-mark" role="img" aria-label="Handwritten signature of the managing director" viewBox="0 0 145 36">
    <rect width="145" height="36" fill="#f1f1f1"/>
  </svg>

  <div class="signer">
    <div class="signer-name">Peter Kranewitt</div>
    <div class="signer-role">Managing Director</div>
  </div>

  <footer class="footer">
    <div class="footer-col">
      <b>Mag. Lukas Fellnhuber</b><br>
      Managing director<br>
      Matthias-Ortner-Strasse 3c / 41<br>
      6300 Wörgl
    </div>
    <div class="footer-col">
      <b>IBAN:</b> AT31 4817 2964 0058 2316<br>
      <b>BIC:</b> GLMTAT44XXX<br>
      <b>Account holder:</b><br>
      KEV Wohnbau &amp; Grundstücksentwicklung GmbH
    </div>
    <div class="footer-col">
      <b>Tel .:</b> +436648172093<br>
      <b>Email:</b> office@wohnglanz-beispiel.at<br>
      <b>Web:</b> www.wohnglanz-beispiel.at<br>
      <b>FN:</b> XXXXXXX | <b>UID:</b> XXXXXXX
    </div>
  </footer>
</main>
</body>
</html>
```